Web Design for Employee Benefits / Corporate Insurance Solutions Firm - Using Divi (by Corvane Pix...

*Please use Divi from corvane pixels to create the design.

Company Name: Harbourline By Tomas(Logo attached)

Colour scheme: White / Teal / Aquamarine / Grey

We are a firm that provides the following solutions for businesses:
- employee medical benefits
- office insurance
- talent retention / long-service retirement solutions
- keyman insurance

We need a website to provide information about our services, as well as password portals for employees of each company that we take care of.

Portals would provide specific information for employees of each company:
- employee handbook
- plan benefits & references
- claim forms

The site would also list articles for Human Resource Professionals and give them information about latest updates in the employee benefits / corporate culture best practices.

Human Resource Executives, Managing Directors, Chief Finance Officers, Employees

Business Consultant

• Should be able to adjust the website widths & font sizes to be viewed on:
• - computer;
• - slatu;
• - smartphone

```html
<!DOCTYPE html>
<html lang="en">
<head>
<meta charset="utf-8">
<title>Harbourline By Tomas – Employee Benefits</title>
<link href="https://fonts.googleapis.com/css2?family=Rubik:wght@400;500;700&display=swap" rel="stylesheet">
<style>
:root{
  --green:#37bc82;
  --green-dark:#2ea672;
  --mint:#e3f6ee;
  --ink:#1c1c1c;
  --grey:#8a8a8a;
  --line:#ececec;
  --white:#ffffff;
}
*{margin:0;padding:0;box-sizing:border-box}
html,body{width:1200px;height:1200px;overflow:hidden;background:var(--white);font-family:"Rubik",sans-serif;color:var(--ink)}
.page{position:absolute;left:422px;top:0;width:377px;height:1200px;background:var(--white);overflow:hidden}
.abs{position:absolute}

/* hero */
.hero{left:0;top:0;width:377px;height:210px;background:linear-gradient(120deg,#2a3338 0%,#4a4d50 35%,#3a4046 60%,#262b31 100%)}
.hero-shade{left:0;top:0;width:377px;height:210px;background:rgba(20,25,30,.35)}
.brand{display:flex;flex-direction:column;align-items:center;gap:2px;color:var(--white);font-weight:500}
.brand .dot{width:14px;height:14px;border-radius:50%;background:var(--green)}
.brand .name{font-size:5.5px;letter-spacing:1.2px;white-space:nowrap}
.header-brand{left:38px;top:7px}
.nav{top:18px;left:162px;display:flex;gap:8px;font-size:3.6px;color:var(--white)}
.btn-login{left:294px;top:16px;width:20px;height:8px;border:.6px solid var(--white);color:var(--white);font-size:3.2px;display:flex;align-items:center;justify-content:center}
.btn-sign{left:318px;top:16px;width:21px;height:8px;background:var(--green);color:var(--white);font-size:3.2px;display:flex;align-items:center;justify-content:center}
.hero-title{left:0;top:82px;width:377px;text-align:center;color:var(--white);font-weight:500;font-size:11.2px;line-height:15px}
.hero-btn{left:169px;top:121px;width:40px;height:11px;background:var(--green);color:var(--white);font-size:3.2px;display:flex;align-items:center;justify-content:center}

/* services */
.divider{left:0;width:377px;height:.8px;background:var(--line)}
.service-title{font-size:8.6px;font-weight:500;line-height:10.8px}
.service-text{margin-top:7px;width:120px;font-size:3.2px;line-height:6.4px;color:var(--grey)}
.service-text p+p{margin-top:3px}
.blob{position:absolute}
.photo{position:absolute;width:84px;height:96px;border-radius:2px;box-shadow:0 2px 6px rgba(0,0,0,.18)}

/* testimonial & footer */
.wave{left:0;top:990px;width:377px;height:210px}
.quote-card{left:70px;top:988px;width:237px;height:99px;background:var(--white);box-shadow:0 2px 8px rgba(0,0,0,.12)}
.quote-photo{left:21px;top:26px;width:51px;height:54px;background:linear-gradient(160deg,#8a7b6c,#3a3430)}
.quote-tri{left:14px;top:20px}
.quote-text{left:82px;top:24px;width:145px;font-size:3.2px;line-height:7px;color:var(--grey)}
.quote-name{left:82px;top:61px;font-size:4.2px;color:var(--green)}
.quote-role{left:82px;top:68px;font-size:3px;color:var(--grey)}
.arrow{width:9px;height:9px;border-radius:50%;display:flex;align-items:center;justify-content:center;font-size:5px}
.arrow.prev{left:210px;top:84px;border:.6px solid var(--line);color:var(--grey)}
.arrow.next{left:222px;top:84px;background:var(--green);color:var(--white)}

.footer-brand{left:42px;top:1100px}
.footer-blurb{left:38px;top:1130px;width:70px;font-size:3px;line-height:6px;color:var(--white);font-weight:500}
.socials{left:46px;top:1160px;display:flex;gap:4px}
.socials span{width:8px;height:8px;border-radius:50%;border:.6px solid rgba(255,255,255,.7)}
.fcol{top:1101px;color:var(--white)}
.fcol h4{font-size:4.4px;font-weight:500;margin-bottom:4px}
.fcol li{list-style:none;font-size:3px;line-height:8.8px}
.fcol li::before{content:"› ";}
.contact-row{display:flex;gap:4px;font-size:3px;line-height:4.4px;margin-bottom:5px}
.contact-row .ic{flex:none;width:6px;height:6px;border-radius:50%;background:rgba(255,255,255,.25);display:flex;align-items:center;justify-content:center}
.bottom-bar{left:0;top:1185px;width:377px;height:15px;background:var(--green-dark);color:var(--white);font-size:3px;display:flex;align-items:center;justify-content:center}
</style>
</head>
<body>
<div class="page">

  <header class="abs hero" role="img" aria-label="Photo of business people meeting around a table"></header>
  <div class="abs hero-shade"></div>
  <div class="abs brand header-brand"><span class="dot"></span><span class="name">HARBOURLINE</span></div>
  <nav class="abs nav"><span>Home</span><span>About Us</span><span>Services</span><span>Testimonial</span><span>Contact us</span></nav>
  <div class="abs btn-login">Login</div>
  <div class="abs btn-sign">Sign up</div>
  <h1 class="abs hero-title">Employee Benefits Corporate<br>Insurance Solutions Firm</h1>
  <div class="abs hero-btn">Contact us</div>

  <!-- Service 1 -->
  <section>
    <svg class="blob" style="left:196px;top:230px" width="123" height="116" viewBox="0 0 123 116"><path d="M20 8 C50 -4 110 0 118 40 C126 80 110 116 70 112 C30 108 6 92 2 60 C-2 30 4 14 20 8Z" fill="var(--mint)"/></svg>
    <div class="photo" style="left:213px;top:239px;background:radial-gradient(circle at 60% 60%,#2d4a6a,#0c1a2c)" role="img" aria-label="Hand pressing a five star rating"></div>
    <div class="abs" style="left:63px;top:245px">
      <h2 class="service-title">Review<br>(Existing Clients Only)</h2>
      <div class="service-text">
        <p>Would you like to know how well your team uses its current employee benefits?</p>
        <p>Do you need clear figures to help plan the budget for the next work year?</p>
        <p>Do you have concerns or issues to raise so we can improve the existing program?</p>
        <p>Tell us and we will gladly come on-site to meet your HR executives and administrators.</p>
      </div>
    </div>
  </section>
  <div class="abs divider" style="top:366px"></div>

  <!-- Service 2 -->
  <section>
    <svg class="blob" style="left:58px;top:386px" width="122" height="116" viewBox="0 0 122 116"><path d="M30 4 C70 -6 118 6 120 40 C122 76 100 112 62 114 C24 116 0 96 2 60 C4 28 12 10 30 4Z" fill="var(--mint)"/></svg>
    <div class="photo" style="left:74px;top:394px;background:linear-gradient(150deg,#5f7d4e,#c9b8b0 60%,#e8e2de)" role="img" aria-label="Consultant on a phone call at her laptop"></div>
    <div class="abs" style="left:200px;top:414px">
      <h2 class="service-title">Consultation<br>(for existing clients only)</h2>
      <div class="service-text" style="width:125px">
        <p>Do you need help with the claim process or a claim outcome?</p>
        <p>Do you need advice or assistance with your personal portfolio?</p>
        <p>Gather a few of your colleagues who want time for a private talk with us, and we will assist on-site.</p>
      </div>
    </div>
  </section>
  <div class="abs divider" style="top:522px"></div>

  <!-- Service 3 -->
  <section>
    <svg class="blob" style="left:196px;top:542px" width="123" height="116" viewBox="0 0 123 116"><path d="M20 8 C50 -4 110 0 118 40 C126 80 110 116 70 112 C30 108 6 92 2 60 C-2 30 4 14 20 8Z" fill="var(--mint)"/></svg>
    <div class="photo" style="left:213px;top:550px;background:linear-gradient(180deg,#a9d3d8 0%,#5f8fa0 45%,#1e3a4c 100%)" role="img" aria-label="Glass office tower seen from below"></div>
    <div class="abs" style="left:63px;top:566px">
      <h2 class="service-title">Draft a<br>New Solution</h2>
      <div class="service-text">
        <p>Are you a new start-up seeking to keep your talent pool with medical benefits?</p>
        <p>Is your current program outdated and do you want a fresh new approach to employee benefits?</p>
        <p>Let's work together to create new solutions that meet the current needs of your employees.</p>
      </div>
    </div>
  </section>
  <div class="abs divider" style="top:677px"></div>

  <!-- Service 4 -->
  <section>
    <svg class="blob" style="left:62px;top:697px" width="122" height="116" viewBox="0 0 122 116"><path d="M30 4 C70 -6 118 6 120 40 C122 76 100 112 62 114 C24 116 0 96 2 60 C4 28 12 10 30 4Z" fill="var(--mint)"/></svg>
    <div class="photo" style="left:78px;top:706px;background:linear-gradient(160deg,#8a6a4a,#b8916a 50%,#4a5560)" role="img" aria-label="Team joining fists over a work table"></div>
    <div class="abs" style="left:203px;top:719px">
      <h2 class="service-title">Review<br>&amp; Assess</h2>
      <div class="service-text" style="width:115px">
        <p>Would you like an unbiased opinion of your current employee benefits program?</p>
        <p>Do you need to review and make improvements to your current employee benefits program?</p>
        <p>Get in touch with us for an initial meeting for this review.</p>
      </div>
    </div>
  </section>
  <div class="abs divider" style="top:832px"></div>

  <!-- Service 5 -->
  <section>
    <svg class="blob" style="left:196px;top:853px" width="123" height="116" viewBox="0 0 123 116"><path d="M20 8 C50 -4 110 0 118 40 C126 80 110 116 70 112 C30 108 6 92 2 60 C-2 30 4 14 20 8Z" fill="var(--mint)"/></svg>
    <div class="photo" style="left:213px;top:862px;background:linear-gradient(180deg,#4a4a4a 0%,#3d5a88 55%,#c9a63a 100%)" role="img" aria-label="Speaker taking notes in a chair"></div>
    <div class="abs" style="left:63px;top:877px">
      <h2 class="service-title">Speaking Engagement<br>(Learning Day)</h2>
      <div class="service-text" style="width:125px">
        <p>Would you like your staff to be more confident with their personal finances?</p>
        <p>How do we enable each employee to use the national framework of health insurance?</p>
        <p>If you would like us to speak and share with your employees, contact us for a talk that meets your needs.</p>
      </div>
    </div>
  </section>

  <!-- Green wave & testimonial -->
  <svg class="abs wave" viewBox="0 0 377 210" preserveAspectRatio="none">
    <path d="M0 8 C40 40 70 70 140 70 C230 70 300 40 377 70 L377 210 L0 210Z" fill="var(--green)"/>
  </svg>

  <div class="abs quote-card">
    <svg class="abs quote-tri" width="66" height="62" viewBox="0 0 66 62"><path d="M33 2 L64 60 L2 60Z" fill="var(--green)"/></svg>
    <div class="abs quote-photo" role="img" aria-label="Portrait of a client in a scarf"></div>
    <p class="abs quote-text">"Working with this team made our benefits review simple and clear. They listened, explained each option and helped our staff understand the plan from day one. We now feel fully supported."</p>
    <div class="abs quote-name">Mara Voss</div>
    <div class="abs quote-role">Client, Voss Studio</div>
    <div class="abs arrow prev">‹</div>
    <div class="abs arrow next">›</div>
  </div>

  <!-- Footer -->
  <div class="abs brand footer-brand"><span class="dot"></span><span class="name">HARBOURLINE</span></div>
  <p class="abs footer-blurb">Benefits and insurance advice for growing firms, with clear plans and friendly support for every team member.</p>
  <div class="abs socials"><span></span><span></span><span></span></div>

  <div class="abs fcol" style="left:129px"><h4>CATEGORY</h4><ul><li>Home</li><li>About Us</li><li>Services</li><li>Testimonial</li><li>Contact Us</li></ul></div>
  <div class="abs fcol" style="left:177px"><h4>INFORMATION</h4><ul><li>Medical</li><li>Office</li><li>Retention</li><li>Keyman</li><li>Claims</li></ul></div>
  <div class="abs fcol" style="left:233px"><h4>NEED HELP?</h4><ul><li>Portal</li><li>Handbook</li><li>Forms</li><li>Articles</li><li>Support</li></ul></div>
  <div class="abs fcol" style="left:285px"><h4>CONTACT US</h4>
    <div class="contact-row"><span class="ic"><svg width="4" height="4" viewBox="0 0 10 10"><path d="M2 1 L4 1 L5 3.5 L3.8 4.5 C4.5 6 5.5 7 6.5 7.2 L7.5 6 L10 7 L10 9 C5 10 0 5 1 1Z" fill="#fff"/></svg></span><span>Phone:<br>020-555-0148</span></div>
    <div class="contact-row"><span class="ic"><svg width="4" height="4" viewBox="0 0 10 10"><rect x="1" y="2.5" width="8" height="5.5" fill="none" stroke="#fff" stroke-width="1"/><path d="M1 2.5 L5 6 L9 2.5" fill="none" stroke="#fff" stroke-width="1"/></svg></span><span>Email:<br>hello@harbourline.example</span></div>
    <div class="contact-row"><span class="ic"><svg width="4" height="4" viewBox="0 0 10 10"><path d="M5 0.5 C2.5 0.5 1.5 2.3 1.5 4 C1.5 6.5 5 9.5 5 9.5 C5 9.5 8.5 6.5 8.5 4 C8.5 2.3 7.5 0.5 5 0.5Z" fill="#fff"/></svg></span><span>Address:<br>12 Quay Road, Harbour City,<br>United Kingdom</span></div>
  </div>

  <div class="abs bottom-bar">© 2018 Harbourline. All rights reserved.</div>
</div>
</body>
</html>
```